Consulting Firm Proposal Template

We need a template for proposals that we send to our clients using the attached outline. Our company is "Brindlemere Consulting Group". We would like a title page with the rest of the information on the following pages. The title page and subsequent pages should be designed in a way to support the use of pictures or graphics. We are looking to use a bold black and white color scheme. Overall we would like the design to confirm our deep experience and knowledge while still following modern design trends.

Target Market(s)

Medium Size Corporations

Industry/Entity Type

Consulting

Logo Text

Brindlemere Consulting Group

Font styles to use
Serif
Sans Serif

Colors

Designer to choose only greyscale colors for use in the design.

Requirements
Must have
• Title Page
Headers
Footers

```html
<!DOCTYPE html>
<html lang="en">
<head>
<meta charset="utf-8">
<title>Brindlemere Consulting Group – Business Proposal</title>
<link rel="stylesheet" href="https://fonts.googleapis.com/css2?family=Playfair+Display:wght@400;700&family=Roboto:wght@300;400;700&display=swap">
<style>
  :root {
    --backdrop: #e4e4e4;
    --paper: #ffffff;
    --ink: #2b2b2b;
    --ink-soft: #555555;
    --ink-faint: #9a9a9a;
    --rule: #cfcfcf;
    --panel: #ececec;
    --tone-1: #d6d6d6;
    --tone-2: #bdbdbd;
    --tone-3: #8c8c8c;
    --tone-4: #5e5e5e;
  }
  * { box-sizing: border-box; margin: 0; padding: 0; }
  html, body { width: 1200px; height: 1000px; overflow: hidden; }
  body {
    background: linear-gradient(180deg, #f1f1f1 0%, var(--backdrop) 100%);
    font-family: "Roboto", Arial, sans-serif;
    color: var(--ink);
    position: relative;
  }
  .spread {
    position: absolute; left: 80px; top: 130px;
    width: 1040px; height: 740px;
    display: flex;
    box-shadow: 0 10px 30px rgba(0,0,0,.12);
  }
  .page { position: relative; width: 520px; height: 740px; background: var(--paper); }
  .page--left { border-right: 1px solid var(--rule); }

  .page-header { position: absolute; top: 34px; left: 40px; right: 40px; height: 26px; border-bottom: 1px solid var(--rule); }
  .page-header__brand { font-family: "Roboto", Arial, sans-serif; font-size: 10px; color: var(--ink-faint); }
  .page-header__title { text-align: right; font-weight: 300; font-size: 15px; color: var(--ink-faint); }

  .icon-row { position: absolute; top: 110px; left: 80px; display: flex; gap: 26px; }
  .icon-slot { width: 44px; height: 44px; border-radius: 50%; background: var(--tone-1); }

  .section-title {
    position: absolute; top: 250px; right: 50px; text-align: right;
    font-family: "Playfair Display", Georgia, serif; font-weight: 400; font-size: 36px; line-height: .95;
    letter-spacing: -1px; color: var(--ink);
  }
  .points { position: absolute; font-size: 12.5px; line-height: 1.6; color: var(--ink-soft); }
  .points--a { top: 330px; left: 58px; width: 165px; }
  .points--b { top: 392px; left: 238px; width: 180px; }
  .point { margin-bottom: 14px; }
  .point__heading { font-weight: 700; font-size: 11.5px; letter-spacing: .5px; color: var(--ink); text-transform: uppercase; line-height: 1.5; }

  .page-footer { position: absolute; bottom: 30px; left: 58px; right: 40px; border-top: 1px solid var(--rule); padding-top: 8px; display: flex; justify-content: space-between; font-size: 9px; color: var(--ink-faint); }
  .page-footer__contact { text-align: right; line-height: 1.5; }

  .solutions-panel { position: absolute; top: 72px; left: 30px; width: 460px; height: 630px; background: var(--panel); }
  .solutions-panel__title { position: absolute; top: 10px; left: 120px; font-family: "Playfair Display", Georgia, serif; font-weight: 700; font-size: 40px; color: var(--ink); }
  .solutions-panel__lead { position: absolute; top: 64px; left: 130px; width: 170px; text-align: center; font-size: 8px; line-height: 1.35; text-transform: uppercase; color: var(--ink-soft); }
  .solutions-diagram { position: absolute; top: 0; left: 0; }

  .offer-table { position: absolute; left: 44px; top: 478px; width: 380px; border-collapse: collapse; font-size: 10px; }
  .offer-table th { background: var(--tone-1); font-weight: 700; text-align: left; padding: 9px 12px; color: var(--ink); }
  .offer-table td { height: 28px; background: #e2e2e2; }
  .offer-table tr:nth-child(even) td { background: var(--tone-1); }
</style>
</head>
<body>
<main class="spread">
  <section class="page page--left">
    <header class="page-header"><span class="page-header__brand">Brindlemere Consulting Group</span></header>

    <div class="icon-row">
      <div class="icon-slot" role="img" aria-label="Line icon of an atom"></div>
      <div class="icon-slot" role="img" aria-label="Line icon of a microscope"></div>
      <div class="icon-slot" role="img" aria-label="Line icon of a brain"></div>
      <div class="icon-slot" role="img" aria-label="Line icon of a light bulb"></div>
    </div>

    <h1 class="section-title">Understanding<br>of the Problem</h1>

    <div class="points points--a">
      <div class="point"><h2 class="point__heading">1. Research &amp;<br>Observations</h2><p>Early in the engagement, our team studied the market, met key staff and mapped every core process.</p></div>
      <div class="point"><h2 class="point__heading">2. Case Study</h2><p>We compared similar firms in the sector, noting what worked, what failed and why, so each lesson could shape the present plan.</p></div>
    </div>
    <div class="points points--b">
      <div class="point"><h2 class="point__heading">3. Problem Solving</h2><p>Findings were ranked by impact and effort, giving a clear order for the work ahead.</p></div>
      <div class="point"><h2 class="point__heading">4. Analysis &amp; Results</h2><p>Each change was measured against agreed targets. Results were reviewed with leadership every month, and the plan was adjusted where needed.</p></div>
    </div>

    <footer class="page-footer">
      <span class="page-footer__number">4</span>
      <span class="page-footer__contact">a: 18 Harrow Lane Millbrook<br>NJ 07110<br>p: +001 02 555 314</span>
    </footer>
  </section>

  <section class="page page--right">
    <header class="page-header"><p class="page-header__title">Business Proposal</p></header>

    <div class="solutions-panel">
      <svg class="solutions-diagram" width="460" height="470" viewBox="0 0 460 470" font-family="Roboto, Arial, sans-serif">
        <g fill="none" stroke="var(--tone-3)" stroke-width="1">
          <path d="M78 138 V150 H205 V190"/>
          <path d="M372 108 V150 H300 V185"/>
          <path d="M395 302 V290 H330"/>
          <path d="M110 352 V330 H165 V290"/>
        </g>
        <circle cx="250" cy="250" r="100" fill="none" stroke="var(--tone-2)" stroke-width="1"/>
        <circle cx="250" cy="250" r="86" fill="none" stroke="var(--tone-2)" stroke-width="5"/>
        <path d="M164 250 A86 86 0 0 1 250 164" fill="none" stroke="var(--tone-3)" stroke-width="5"/>
        <circle cx="250" cy="250" r="62" fill="none" stroke="var(--tone-2)" stroke-width="16"/>
        <path d="M188 250 A62 62 0 0 0 312 250" fill="none" stroke="var(--tone-4)" stroke-width="16"/>
        <circle cx="250" cy="250" r="54" fill="var(--tone-1)"/>
        <circle cx="165" cy="290" r="4" fill="var(--panel)" stroke="var(--tone-3)"/>
        <text x="250" y="247" text-anchor="middle" font-size="8" font-weight="700" fill="var(--ink)">COMPANY</text>
        <text x="250" y="258" text-anchor="middle" font-size="8" font-weight="700" fill="var(--ink)">PROBLEM</text>

        <g>
          <circle cx="78" cy="100" r="38" fill="none" stroke="var(--tone-2)" stroke-width="2"/>
          <circle cx="78" cy="100" r="28" fill="var(--tone-1)" role="img" aria-label="Icon of a certificate"/>
          <text x="84" y="56" font-size="7" fill="var(--ink-soft)">( X + 1</text>
          <text x="40" y="168" font-size="9" font-weight="700" fill="var(--ink)">RESEARCH &amp; OBSERVATION</text>
          <text x="40" y="180" font-size="8" fill="var(--ink-soft)">We gather data, interview staff</text>
          <text x="40" y="190" font-size="8" fill="var(--ink-soft)">and observe daily operations</text>
          <text x="40" y="200" font-size="8" fill="var(--ink-soft)">before drawing conclusions</text>
        </g>
        <g>
          <circle cx="372" cy="70" r="38" fill="none" stroke="var(--tone-2)" stroke-width="2"/>
          <circle cx="372" cy="70" r="28" fill="var(--tone-1)" role="img" aria-label="Icon of a clipboard and pen"/>
          <text x="385" y="118" font-size="7" fill="var(--ink-soft)">X2 + (X + 1)</text>
          <text x="330" y="128" font-size="9" font-weight="700" fill="var(--ink)">CASE STUDY</text>
          <text x="330" y="140" font-size="8" fill="var(--ink-soft)">Similar firms</text>
          <text x="330" y="150" font-size="8" fill="var(--ink-soft)">in the sector are</text>
          <text x="330" y="160" font-size="8" fill="var(--ink-soft)">studied to learn</text>
          <text x="330" y="170" font-size="8" fill="var(--ink-soft)">which approaches</text>
          <text x="330" y="180" font-size="8" fill="var(--ink-soft)">worked and which</text>
          <text x="330" y="190" font-size="8" fill="var(--ink-soft)">did not.</text>
        </g>
        <g>
          <text x="355" y="225" font-size="9" font-weight="700" fill="var(--ink)">PROBLEM SOLVING</text>
          <circle cx="395" cy="340" r="38" fill="none" stroke="var(--tone-2)" stroke-width="2"/>
          <circle cx="395" cy="340" r="28" fill="var(--tone-1)" role="img" aria-label="Icon of a laboratory flask"/>
          <text x="335" y="375" font-size="7" fill="var(--ink-soft)">X3 + (X2 +</text>
          <text x="345" y="384" font-size="7" fill="var(--ink-soft)">(X + 1))</text>
        </g>
        <g>
          <text x="60" y="310" font-size="9" font-weight="700" fill="var(--ink)">RESULTS &amp;</text>
          <text x="60" y="321" font-size="9" font-weight="700" fill="var(--ink)">ANALYSIS</text>
          <circle cx="110" cy="390" r="38" fill="none" stroke="var(--tone-2)" stroke-width="2"/>
          <circle cx="110" cy="390" r="28" fill="none" stroke="var(--tone-4)" stroke-width="5"/>
          <circle cx="110" cy="390" r="22" fill="var(--tone-1)" role="img" aria-label="Icon of a checklist with a tick"/>
          <text x="158" y="385" font-size="7" fill="var(--ink-soft)">X4 + (X3 +</text>
          <text x="158" y="394" font-size="7" fill="var(--ink-soft)">(X2 + (X + 1))</text>
        </g>
      </svg>

      <h2 class="solutions-panel__title">Solutions</h2>
      <p class="solutions-panel__lead">Four linked stages move every engagement from first question to result</p>

      <table class="offer-table">
        <thead><tr><th>Package</th><th>Product Service</th><th>Benefit</th></tr></thead>
        <tbody>
          <tr><td></td><td></td><td></td></tr>
          <tr><td></td><td></td><td></td></tr>
          <tr><td></td><td></td><td></td></tr>
          <tr><td></td><td></td><td></td></tr>
        </tbody>
      </table>
    </div>
  </section>
</main>
</body>
</html>
```